Need Business Cards for my Business

email address: rkpmarlowhollowworks@vendrimail.com
web address: rkpmarlowhollowworks.net
Slogan: We offer various QVN licenses
Rowland K. Pemberly
Please stick with colors of Company Logo
would like the card to be more of the color example of the logo.
If you need PDF copy of logo email me at the above account.
Creative control rests with you.

Industry/Entity Type

Business

Contact Information for Business Card

I am a minimalist, but would like something to pop and stand out amongst other cards, make it memorable.

Font styles to use
Serif
Decorative
Script

```html
<!DOCTYPE html>
<html lang="en">
<head>
<meta charset="utf-8">
<title>Rowland K. Pemberly — Business Cards</title>
<link rel="stylesheet" href="https://fonts.googleapis.com/css2?family=Lora:wght@400;500&display=swap">
<style>
  :root {
    --page-bg: #ffffff;
    --card-light: #ffffff;
    --card-shade: #efefef;
    --ink: #111418;
    --brand-blue: #357cc0;
    --brand-navy: #2c4668;
    --brand-red: #e8383c;
  }
  * { margin: 0; padding: 0; box-sizing: border-box; }
  html, body {
    width: 1200px;
    height: 1000px;
    overflow: hidden;
    background: var(--page-bg);
    font-family: "Lora", Georgia, serif;
    color: var(--ink);
  }
  .card {
    position: absolute;
    left: 286px;
    width: 631px;
    height: 361px;
    background: linear-gradient(200deg, var(--card-shade) 0%, var(--card-light) 55%, var(--card-light) 100%);
    box-shadow: 4px 5px 7px rgba(0, 0, 0, 0.55);
    overflow: hidden;
  }
  .card--front { top: 89px; }
  .card--back { top: 542px; }

  .accent-bands {
    position: absolute;
    inset: 0;
    width: 631px;
    height: 361px;
  }
  .band--blue { fill: url(#blueFade); }
  .band--red { fill: var(--brand-red); }

  .holder-name {
    position: absolute;
    left: 50px;
    top: 84px;
    font-size: 26px;
    font-weight: 400;
    letter-spacing: 0.2px;
  }
  .contact-list {
    position: absolute;
    left: 49px;
    top: 188px;
    list-style: none;
  }
  .contact-item {
    display: flex;
    align-items: center;
    height: 20px;
    margin-bottom: 14px;
    font-size: 13px;
  }
  .contact-item svg {
    width: 18px;
    height: 18px;
    margin-right: 13px;
    flex: none;
    fill: var(--brand-blue);
  }

  .brand-lockup {
    position: absolute;
    left: 0;
    right: 0;
    top: 132px;
    display: flex;
    align-items: center;
    justify-content: center;
    gap: 16px;
  }
  .brand-dot {
    width: 28px;
    height: 28px;
    border-radius: 50%;
    background: var(--brand-red);
  }
  .brand-name {
    font-size: 34px;
    font-weight: 500;
    color: var(--brand-navy);
    letter-spacing: 0.4px;
  }
  .slogan {
    position: absolute;
    left: 0;
    right: 0;
    top: 313px;
    text-align: center;
    font-size: 20px;
  }
</style>
</head>
<body>
  <section class="card card--front">
    <svg class="accent-bands" viewBox="0 0 631 361" aria-hidden="true">
      <defs>
        <linearGradient id="blueFade" x1="0" y1="0" x2="0" y2="1">
          <stop offset="0" stop-color="#357cc0"/>
          <stop offset="1" stop-color="#2c4668"/>
        </linearGradient>
      </defs>
      <polygon class="band band--blue" points="392,0 470,0 631,161 631,325"/>
      <polygon class="band band--red" points="328,0 368,0 631,263 631,303"/>
    </svg>
    <h1 class="holder-name">Rowland K. Pemberly</h1>
    <ul class="contact-list">
      <li class="contact-item">
        <svg viewBox="0 0 18 18" aria-hidden="true"><path d="M5 1h8a2 2 0 0 1 2 2v12a2 2 0 0 1-2 2H5a2 2 0 0 1-2-2V3a2 2 0 0 1 2-2zm0 2v11h8V3zm3 12.2h2v1H8z"/></svg>
        <span>555013742</span>
      </li>
      <li class="contact-item">
        <svg viewBox="0 0 18 18" aria-hidden="true"><path d="M9 1a8 8 0 1 0 0 16A8 8 0 0 0 9 1zm5.9 7.2h-2.5a12 12 0 0 0-1-4.6 6.5 6.5 0 0 1 3.5 4.6zM9 2.6c.8 1 1.5 3 1.6 5.6H7.4C7.5 5.6 8.2 3.6 9 2.6zM6.6 3.6a12 12 0 0 0-1 4.6H3.1a6.5 6.5 0 0 1 3.5-4.6zM3.1 9.8h2.5a12 12 0 0 0 1 4.6 6.5 6.5 0 0 1-3.5-4.6zM9 15.4c-.8-1-1.5-3-1.6-5.6h3.2c-.1 2.6-.8 4.6-1.6 5.6zm2.4-1a12 12 0 0 0 1-4.6h2.5a6.5 6.5 0 0 1-3.5 4.6z"/></svg>
        <span>rkpmarlowhollowworks.net</span>
      </li>
      <li class="contact-item">
        <svg viewBox="0 0 18 18" aria-hidden="true"><path d="M0 3h18v1.2L9 10 0 4.2zm0 3 9 5.8L18 6v9H0z"/></svg>
        <span>rkpmarlowhollowworks@vendrimail.com</span>
      </li>
    </ul>
  </section>

  <section class="card card--back">
    <div class="brand-lockup">
      <span class="brand-dot"></span>
      <span class="brand-name">RKP Marlow Hollow Works</span>
    </div>
    <p class="slogan">We offer various QVN licenses</p>
  </section>
</body>
</html>
```